Personal training and nutrition business needs business card design

We need a business card that outlays our services and invites potential customers to join our team and take the first step to a healthier and more enjoyable life. We cater for any level of fitness and specialize in weight loss and conditioning, strength training, muscle gain and strength endurance. Whether you are just starting off or need some help getting to the next level of your journey we are here to get the job done.
We specialize in one on one or one on two personal training sessions and each program will be custom made to suit individual fitness goals of our clients

```html
<!DOCTYPE html>
<html lang="en">
<head>
<meta charset="utf-8">
<title>Stride &amp; Steady – Business Card</title>
<link href="https://fonts.googleapis.com/css2?family=Saira+Condensed:wght@800&family=Oswald:wght@500&family=Raleway:wght@500;600&family=Arimo&display=swap" rel="stylesheet">
<style>
  :root {
    --stage: #2b2b2d;
    --card-dark: #050505;
    --card-light: #ffffff;
    --purple: #7b4fbf;
    --violet: #b363c4;
    --purple-faint: #ece4f3;
    --ink: #161616;
    --grey: #555555;
    --white: #ffffff;
  }
  * { margin: 0; padding: 0; box-sizing: border-box; }
  html, body { width: 1200px; height: 900px; overflow: hidden; }
  body { background: var(--stage); position: relative; }

  .card {
    position: absolute;
    left: 270px;
    width: 660px;
    height: 377px;
    overflow: hidden;
    box-shadow: 0 10px 30px rgba(0,0,0,.45);
  }
  .card--front { top: 48px; background: var(--card-dark); }
  .card--back  { top: 470px; background: var(--card-light); }

  .brand { display: flex; align-items: center; gap: 12px; }
  .brand__dot { width: 30px; height: 30px; border-radius: 50%; background: var(--purple); flex: none; }
  .brand__name {
    font-family: "Saira Condensed", sans-serif;
    font-weight: 800;
    text-transform: uppercase;
    line-height: 1;
  }
  .tagline {
    font-family: "Oswald", sans-serif;
    font-weight: 500;
    color: var(--violet);
    text-transform: uppercase;
    letter-spacing: .08em;
  }

  /* front */
  .card--front .front-brand {
    position: absolute; left: 0; right: 0; top: 130px;
    display: flex; flex-direction: column; align-items: center; gap: 12px;
  }
  .card--front .brand__name { color: var(--white); font-size: 50px; }
  .card--front .tagline { font-size: 12px; }

  /* back */
  .back-brand { position: absolute; left: 40px; top: 50px; }
  .card--back .brand__name { color: var(--ink); font-size: 36px; }
  .card--back .tagline { font-size: 9px; margin-top: 8px; }

  .contact {
    position: absolute; left: 42px; top: 220px;
    font-family: "Arimo", sans-serif; color: var(--ink);
    font-size: 17px; list-style: none;
  }
  .contact li { display: flex; align-items: flex-start; gap: 18px; line-height: 1.25; }
  .contact li + li { margin-top: 4px; }
  .contact .address { margin-bottom: 18px; }
  .contact svg { width: 16px; height: 16px; flex: none; margin-top: 2px; fill: var(--purple); }

  .person { position: absolute; right: 44px; top: 96px; text-align: right; }
  .person__name {
    font-family: "Raleway", sans-serif; font-weight: 600;
    font-size: 22px; color: var(--purple);
  }
  .person__role { font-family: "Raleway", sans-serif; font-weight: 500; font-size: 13px; color: var(--grey); margin-top: 2px; }
  .tab {
    position: absolute; right: 0; top: 80px; width: 20px; height: 58px;
    background: var(--violet); border-radius: 10px 0 0 10px;
  }
  .watermark-shape {
    position: absolute; right: 34px; bottom: 40px;
    width: 170px; height: 170px; border-radius: 50%;
    background: var(--purple-faint);
  }
</style>
</head>
<body>

<section class="card card--front" aria-label="Card front">
  <div class="front-brand">
    <div class="brand">
      <span class="brand__dot"></span>
      <span class="brand__name">Stride &amp; Steady</span>
    </div>
    <p class="tagline">Personal training. Nutrition. Motivation</p>
  </div>
</section>

<section class="card card--back" aria-label="Card back">
  <div class="back-brand">
    <div class="brand">
      <span class="brand__dot"></span>
      <span class="brand__name">Stride &amp; Steady</span>
    </div>
    <p class="tagline">Personal training. Nutrition. Motivation</p>
  </div>

  <ul class="contact">
    <li class="address">
      <svg viewBox="0 0 16 16" aria-hidden="true"><path d="M8 0a5 5 0 0 0-5 5c0 4 5 11 5 11s5-7 5-11a5 5 0 0 0-5-5zm0 7.2A2.2 2.2 0 1 1 8 2.8a2.2 2.2 0 0 1 0 4.4z"/></svg>
      <span>Harbor Pointe Plaza,<br>Clearwater, Florida 33760</span>
    </li>
    <li>
      <svg viewBox="0 0 16 16" aria-hidden="true"><path d="M3.6 1l2.3 2.8-1.4 1.8a9 9 0 0 0 5.9 5.9l1.8-1.4L15 12.4 13.2 15C6.6 14.4 1.6 9.4 1 2.8z"/></svg>
      <span>014 2233 5566</span>
    </li>
    <li>
      <svg viewBox="0 0 16 16" aria-hidden="true"><path d="M1 3h14v10H1zm1.5 1.2L8 8.6l5.5-4.4z"/></svg>
      <span>info@strideandsteady.com</span>
    </li>
    <li>
      <svg viewBox="0 0 16 16" aria-hidden="true"><circle cx="8" cy="8" r="7"/><path d="M1 8h14M8 1c3 3 3 11 0 14M8 1c-3 3-3 11 0 14" stroke="#fff" stroke-width="1" fill="none"/></svg>
      <span>www.strideandsteady.com</span>
    </li>
  </ul>

  <div class="tab"></div>
  <div class="person">
    <p class="person__name">Marcus Lenfield</p>
    <p class="person__role">Director</p>
  </div>

  <div class="watermark-shape"></div>
</section>

</body>
</html>
```